8 1/2 x 11 Flyer Design for Water Damage Restoration Company

Houston Texas based Water Damage Restoration company is needing a advertising flyer that highlights water damage and water extraction.

KESTRAL Emergency Services
52710 Harlow Crossing Suite G4
Houston, Texas 77193
713-846-5170
www.KESTRAL58129.example

Water Damage Restoration
Water Extraction
Mold Prevention
24/7/365
FREE Evaluations

Suggested photos to use:
Water Damage
Leaking Pipes
Water on floors and ground
Water pouring from ceilings
Technicians
Company Logo
Photos

Company Colors:
Orange and Blue

```html
<!DOCTYPE html>
<html lang="en">
<head>
<meta charset="utf-8">
<title>KESTRAL Emergency Services – Water Damage Flyer</title>
<link rel="stylesheet" href="https://fonts.googleapis.com/css2?family=Montserrat:wght@700;800&family=Questrial&display=swap">
<style>
:root{
  --navy:#1c2d5e;
  --orange:#f26a1b;
  --white:#ffffff;
  --mist:#eef2f8;
  --rim:#e9ebef;
  --band:#e6e7ea;
  --ink:#1c2d5e;
  --stage:#3c3c3c;
}
*{box-sizing:border-box;margin:0;padding:0}
html,body{width:973px;height:1200px;overflow:hidden;background:var(--stage)}
.flyer{position:absolute;left:21px;top:0;width:931px;height:1200px;overflow:hidden;background:linear-gradient(180deg,var(--navy) 0,var(--navy) 540px,#dfe7f3 560px,var(--white) 1000px);font-family:"Questrial",sans-serif;color:var(--ink)}
.backdrop{position:absolute;inset:0}
.brand{position:absolute;left:58px;top:62px;color:var(--navy);font-family:"Montserrat",sans-serif;font-weight:800;line-height:1}
.brand .name{display:block;font-size:54px;letter-spacing:1px}
.brand .sub{display:block;font-size:19px;margin-top:8px;letter-spacing:.3px}
.headline{position:absolute;left:56px;top:234px;font-family:"Montserrat",sans-serif;font-weight:800;font-size:44px;line-height:52px;color:var(--orange);letter-spacing:.3px;white-space:nowrap}
.tagline{position:absolute;left:56px;top:396px;font-size:25px;line-height:30px;color:var(--white);white-space:nowrap}
.hero{position:absolute;left:487px;top:0;width:444px;height:630px}
.photo-circle{position:absolute;border-radius:50%;border:7px solid var(--rim);box-shadow:0 6px 14px rgba(0,0,0,.18)}
.c1{left:50px;top:500px;width:166px;height:166px;background:radial-gradient(circle at 40% 40%,#c9b9a2,#6e5437 70%,#3a2c20)}
.c2{left:245px;top:506px;width:200px;height:200px;background:radial-gradient(circle at 50% 35%,#a8906e,#4b3a2a 55%,#2f4c86 85%)}
.c3{left:461px;top:467px;width:186px;height:186px;background:linear-gradient(180deg,#f1f1f1 0,#d9d9d9 55%,#8f8a80 75%,#6e6a62)}
.about{position:absolute;left:56px;top:742px;width:412px;font-size:17.5px;line-height:23px;color:#22284a}
.specialties{position:absolute;left:56px;top:896px;font-size:23.5px;line-height:30px;color:var(--navy);white-space:nowrap}
.specialties .sep{color:var(--orange);margin:0 6px}
.call{position:absolute;left:56px;top:982px;font-size:33px;line-height:40px;color:var(--navy)}
.phone{position:absolute;left:51px;top:1030px;display:flex;align-items:center;gap:12px}
.phone .icon{width:44px;height:44px}
.phone .number{font-family:"Montserrat",sans-serif;font-weight:700;font-size:45px;color:var(--orange);letter-spacing:-.5px;white-space:nowrap}
.services{position:absolute;left:560px;top:721px;width:322px;height:313px;border:1.5px solid #c8ccd6;border-radius:14px;background:rgba(255,255,255,.55)}
.services-tab{position:absolute;left:559px;top:699px;width:237px;height:40px;background:var(--orange);border-radius:0 26px 0 0;color:var(--white);font-family:"Montserrat",sans-serif;font-weight:800;font-size:23px;line-height:41px;padding-left:26px}
.service-list{position:absolute;left:590px;top:760px;list-style:none}
.service-list li{display:flex;align-items:center;gap:20px;font-size:23px;line-height:28px;color:var(--navy);margin-bottom:20px;white-space:nowrap}
.service-list li:first-child{margin-bottom:16px}
.service-list svg{width:34px;height:34px;flex:none}
.credentials{position:absolute;left:561px;top:1052px;font-size:20.5px;color:var(--navy);display:flex;align-items:center;gap:7px;letter-spacing:-.2px;white-space:nowrap}
.credentials .dot{width:11px;height:11px;border:3px solid var(--orange);border-radius:50%}
.address-band{position:absolute;left:0;top:1129px;width:480px;height:54px;background:var(--band)}
.address{position:absolute;left:50px;top:1136px;display:flex;gap:10px;font-size:18px;line-height:20px;color:#222;white-space:nowrap}
.address svg{width:18px;height:24px;margin-top:6px}
.web-block{position:absolute;left:471px;top:1110px;width:460px;height:90px}
.web{position:absolute;left:500px;top:1136px;width:420px;text-align:center;font-size:24px;line-height:32px;color:var(--white);letter-spacing:-.3px;white-space:nowrap}
.web b{font-family:"Montserrat",sans-serif;font-weight:800}
</style>
</head>
<body>
<main class="flyer">
  <svg class="backdrop" width="931" height="1200" viewBox="0 0 931 1200" aria-hidden="true">
    <path d="M0 560 Q120 545 240 565 T480 560 T931 545 L931 1200 L0 1200 Z" fill="#f4f7fb"/>
    <ellipse cx="190" cy="-56" rx="237" ry="258" fill="var(--orange)"/>
    <ellipse cx="190" cy="-62" rx="235" ry="254" fill="#f5f6fa"/>
  </svg>

  <div class="brand"><span class="name">KESTRAL</span><span class="sub">EMERGENCY SERVICES</span></div>

  <h1 class="headline">WATER DAMAGE<br>RESTORATION<br>IN HOUSTON</h1>
  <p class="tagline">Fast &amp; Reliable Residential<br>and Commercial Services</p>

  <svg class="hero" viewBox="0 0 444 630">
    <defs>
      <linearGradient id="heroPhoto" x1="0" y1="0" x2="1" y2="1">
        <stop offset="0" stop-color="#d8dadf"/>
        <stop offset=".5" stop-color="#b9b3ad"/>
        <stop offset=".8" stop-color="#3046a8"/>
        <stop offset="1" stop-color="#6b6460"/>
      </linearGradient>
    </defs>
    <path d="M58 0 L283 0 Q444 150 444 262 L444 560 Q380 632 210 628 Q0 622 0 420 Q0 250 58 0 Z" fill="var(--rim)"/>
    <path role="img" aria-label="Photo: woman on the phone holding a bucket under water leaking from the ceiling" d="M84 0 L270 0 Q444 160 444 270 L444 548 Q370 612 215 606 Q26 600 26 420 Q26 250 84 0 Z" fill="url(#heroPhoto)"/>
    <path d="M115 0 L124 0 Q78 200 84 360 Q90 520 230 590 Q110 560 72 440 Q48 300 115 0 Z" fill="var(--orange)"/>
  </svg>

  <div class="photo-circle c1" role="img" aria-label="Photo: water-damaged wall and rotted framing"></div>
  <div class="photo-circle c2" role="img" aria-label="Photo: technician catching water from a damaged ceiling"></div>
  <div class="photo-circle c3" role="img" aria-label="Photo: flooded modern kitchen"></div>

  <p class="about">KESTRAL Emergency Services is a full-service water damage company in Houston. Our services include restoration, storm cleanup, biohazard cleanup, and fire damage restoration service. We cater to the needs of customers throughout the Greater Houston and surrounding areas.</p>

  <p class="specialties">Water Damage<span class="sep">|</span>Flood<span class="sep">|</span>Fire<span class="sep">|</span>Smoke<br>Mold Prevention Specialist</p>

  <p class="call">Call us Today</p>
  <div class="phone">
    <svg class="icon" viewBox="0 0 44 44" aria-hidden="true">
      <circle cx="22" cy="22" r="22" fill="var(--navy)"/>
      <path d="M15 11 l5 5 -3 3 q2 5 7 8 l3 -3 5 5 -3 4 q-10 0 -17 -10 q-3 -6 3 -12z" fill="var(--orange)"/>
      <path d="M25 12 a8 8 0 0 1 7 7 M25 7 a13 13 0 0 1 12 12" stroke="var(--orange)" stroke-width="2" fill="none"/>
    </svg>
    <span class="number">713-846-5170</span>
  </div>

  <div class="services"></div>
  <div class="services-tab">OUR SEVICES</div>
  <ul class="service-list">
    <li><svg viewBox="0 0 34 34" fill="none" stroke="var(--orange)" stroke-width="2"><path d="M3 6h8v6h12V6h8M17 12v6q0 6-6 6M11 24l0 7"/><path d="M24 18q2 3 0 5q-2-2 0-5z"/></svg>Water Damage<br>Restoration</li>
    <li><svg viewBox="0 0 34 34" fill="none" stroke="var(--orange)" stroke-width="2"><rect x="4" y="8" width="26" height="10" rx="2"/><circle cx="17" cy="13" r="4"/><path d="M8 18v8h18v-8M12 26v4h10v-4"/></svg>Water Extraction</li>
    <li><svg viewBox="0 0 34 34" fill="none" stroke="var(--orange)" stroke-width="2"><circle cx="17" cy="17" r="14"/><path d="M7 7l20 20"/><circle cx="14" cy="14" r="2"/><circle cx="21" cy="20" r="2.5"/></svg>Mold Prevention</li>
    <li><svg viewBox="0 0 34 34" fill="none" stroke="var(--orange)" stroke-width="2"><path d="M28 10a13 13 0 1 1-6-6"/><path d="M20 2l3 3-3 3"/><text x="4" y="19" font-size="9" fill="var(--orange)" stroke="none" font-family="Montserrat,sans-serif" font-weight="700">24/7</text></svg>24/7/365</li>
    <li><svg viewBox="0 0 34 34" fill="none" stroke="var(--orange)" stroke-width="2"><rect x="6" y="4" width="20" height="26" rx="2"/><circle cx="16" cy="17" r="6"/><path d="M13 17l2 2 4-4M20 22l6 6"/></svg>FREE Evaluations</li>
  </ul>

  <p class="credentials">LICENSED <span class="dot"></span> BONDED <span class="dot"></span> INSURED</p>

  <div class="address-band"></div>
  <div class="address">
    <svg viewBox="0 0 18 24" aria-hidden="true"><path d="M9 0a9 9 0 0 1 9 9c0 6-9 15-9 15S0 15 0 9a9 9 0 0 1 9-9z" fill="var(--orange)"/><circle cx="9" cy="9" r="3.5" fill="#fff"/></svg>
    <p>52710 Harlow Crossing Suite G4<br>Houston, Texas 77193</p>
  </div>

  <svg class="web-block" viewBox="0 0 460 90" aria-hidden="true">
    <path d="M0 90 Q0 0 80 0 L460 0 L460 90 Z" fill="var(--orange)"/>
    <path d="M10 90 Q12 10 90 7 L460 7 L460 90 Z" fill="var(--navy)"/>
  </svg>
  <p class="web">www.<b>KESTRAL58129</b>.example</p>
</main>
</body>
</html>
```